velmorino.eu :: Design ideas (no coding) for key pages of Personalized greeting cards online store

We need your vision on modern, clean, easy to read user interface (UI) for online service of personalized printed products, like greeting cards, postcards, fridge magnets, clips and etc.
Your vision should include UI presentation for:
- Home page with login (including soc nets)
- Product Designer page
- Cart pages (products and address selection)
- Example of general internal page (pricing, terms, etc)
- Artist info and portfolio page
We are looking for ideas we will love, NOT complete design of a whole site.
Top design/vision will we used as a basement for separate contract on complete design of the site.

UI should be based on existing functionality with some extent. It should not break ideas or methods used on prototype but designers are free to offer own product presentations, designer’s layout and cart views.

Prototype:
English: http://velmorino.eu
Russian: http://velmorino.ru
Lithuanian: http://velmorino.lt

Target Market(s)

People of 16-45 y.o. who likes to be distinctive, personal.

Industry/Entity Type

Store

Requirements
Must have
• Your work should meet attached requirements.
Site is multilingual. Wording should assume varieties in length on different languages.
Clean and easy to read UI
Flat design preferrably
Should be based on assets which are free or available for royalty-free licensing
Should not have
• heavy, meaningless 3D and shadow effects
Show NOT copy sites like: plonkra.com, tarnwick.co.uk

```html
<!DOCTYPE html>
<html lang="en">
<head>
<meta charset="utf-8">
<title>velmorino — Card Designer</title>
<link href="https://fonts.googleapis.com/css2?family=Source+Sans+3:wght@400;600;700&family=Ubuntu:wght@400&family=Dancing+Script:wght@500&display=swap" rel="stylesheet">
<style>
:root{
  --red:#b52a1c;
  --red-dark:#9c2116;
  --ink:#333;
  --muted:#666;
  --line:#e2e2e2;
  --pink:#fde9e8;
  --hint:#fddf94;
  --page:#f4f3f2;
  --white:#fff;
}
*{box-sizing:border-box;margin:0;padding:0}
html,body{width:1200px;height:1189px;overflow:hidden}
body{position:relative;background:var(--page);font-family:"Source Sans 3",sans-serif;color:var(--ink);font-size:13px}
.abs{position:absolute}
.brand{left:110px;top:88px;display:flex;align-items:center;gap:8px;color:var(--red);font-size:24px;font-weight:400;line-height:1}
.brand-mark{width:14px;height:14px;background:var(--red)}
.tagline{left:0;width:1147px;top:46px;text-align:center;font-family:"Ubuntu",sans-serif;color:var(--red);font-size:18px}
.nav-tab{top:94px;height:35px;line-height:38px;font-weight:700;font-size:14px}
.nav-tab.active{left:256px;width:103px;background:var(--red);color:var(--white);text-align:center;border-radius:4px 4px 0 0}
.nav-tab.plain{left:377px;color:var(--ink)}
.account{top:102px;right:110px;display:flex;gap:20px;font-size:14px;color:var(--muted);align-items:center}
.account b{color:var(--red)}
.account .cart{color:var(--ink)}
.rule{left:110px;width:980px;top:128px;height:2px;background:var(--red)}
.panel{left:110px;width:980px;top:130px;height:803px;background:var(--white);border:1px solid var(--line);border-top:0}
.back{left:135px;top:146px;width:59px;height:22px;background:var(--red);color:#fff;border-radius:3px;font-size:13px;line-height:22px;padding-left:8px}
.crumbs{left:205px;top:150px;font-size:13px;color:var(--muted)}
.crumbs b{color:var(--ink);font-weight:600}
.info{left:1024px;top:160px;font-size:13px;color:var(--muted);display:flex;gap:5px;align-items:center}
.stage{left:135px;top:189px;width:648px;height:558px;border:1px solid var(--line);
  background-color:#fafafa;
  background-image:linear-gradient(#ececec 1px,transparent 1px),linear-gradient(90deg,#ececec 1px,transparent 1px);
  background-size:10px 10px}
.toolbar{left:267px;top:189px;width:399px;height:33px;background:var(--pink);display:flex}
.tool{flex:1 1 auto;display:flex;align-items:center;justify-content:center;gap:6px;font-weight:600;font-size:13px;border-right:1px solid #f2cfcc}
.tool:last-child{border-right:0}
.card-art{left:312px;top:248px;width:297px;height:437px;background:radial-gradient(circle at 45% 45%,#e9e0c8 0 22%,#5f8a3c 30%,#c8312a 45%,#cf3328 100%)}
.side-label{left:366px;top:715px;width:186px;height:32px;background:var(--pink);text-align:center;line-height:32px;font-size:16px;font-weight:600}
.hint{left:135px;top:340px;width:142px;height:189px;background:var(--hint);border-radius:0 4px 4px 0;padding:12px 12px 0 12px}
.hint h3{font-weight:400;font-size:16px;display:flex;align-items:center;gap:5px;margin-bottom:8px}
.hint .close{position:absolute;right:12px;top:10px;font-size:14px}
.hint p{font-size:11.5px;line-height:20px}
.swatches{left:610px;top:459px;width:175px;height:169px;background:#fff;border:1px solid var(--line);padding:16px 0 0 20px;display:grid;grid-template-columns:repeat(4,30px);gap:6px 6px}
.swatches i{width:31px;height:31px;display:block}
.tab{background:var(--pink);font-weight:600;font-size:18px;padding:6px 14px;height:31px;line-height:20px}
.sides-tab{left:800px;top:187px;width:75px}
.sides-box{left:800px;top:218px;width:265px;height:195px;border:1px solid var(--line);background:#fff}
.side{position:absolute;width:76px;height:88px;text-align:center;font-size:11.5px;color:var(--muted);font-weight:600}
.side.on{background:#f0f0f0}
.side svg{display:block;margin:12px auto 6px}
.items-tab{left:800px;top:428px;width:85px;display:flex;gap:6px;align-items:center}
.items-box{left:800px;top:459px;width:265px;height:223px;border:1px solid var(--line);background:#fff}
.opacity{left:815px;top:519px;width:152px;height:34px;border:1px solid var(--line);font-weight:600;font-size:13px;padding:9px 12px}
.bar{left:882px;top:529px;width:74px;height:14px;background:#bbb}
.bar i{display:block;width:52px;height:14px;background:var(--red)}
.pct{left:915px;top:551px;width:36px;height:15px;background:var(--red);color:#fff;font-size:9px;font-weight:700;text-align:center;line-height:15px}
.fonts-btn{left:974px;top:519px;width:76px;height:34px;background:#f2f2f2;font-family:"Dancing Script",cursive;font-size:18px;text-align:center;line-height:34px}
.textarea{left:816px;top:561px;width:233px;height:77px;border:1px solid var(--line)}
.btn{top:646px;width:113px;height:28px;border:1px solid var(--line);text-align:center;line-height:27px;font-size:12.5px;font-weight:600}
.save{left:800px;top:696px;width:265px;height:51px;background:var(--red);color:#fff;display:flex;align-items:center;font-weight:700;font-size:14.5px}
.save .icon{width:78px;height:51px;background:var(--red-dark);display:flex;align-items:center;justify-content:center;margin-right:16px}
.instructions{left:135px;top:766px;width:931px;height:145px;background:var(--pink);padding:12px 14px}
.instructions h3{color:var(--red);font-size:16px;font-weight:600;display:flex;gap:6px;align-items:center;margin-bottom:8px}
.instructions p{font-size:13px;line-height:21px;color:#444}
.footer{left:0;top:948px;width:1200px;height:200px;background:#f7f7f7;border-top:1px solid var(--line)}
.col{top:958px}
.col h4{font-size:14.5px;font-weight:600;color:#444;margin-bottom:8px}
.col li{list-style:none;font-size:12px;color:var(--muted);line-height:21px}
.social{left:899px;top:989px;display:flex;gap:14px}
.social span{width:46px;height:46px;border-radius:50%;color:#fff;font-size:10px;font-weight:600;display:flex;align-items:center;justify-content:center}
.pay{left:493px;top:1094px;width:345px;height:40px;background:#f0ece0;display:flex;gap:11px;padding:4px 3px}
.pay span{width:60px;height:34px;border:1px solid #ccc;background:#fff;font-size:12px;font-weight:700;color:#345;display:flex;align-items:center;justify-content:center}
.copy{left:0;top:1148px;width:1200px;height:41px;background:#f1f1f1;border-top:1px solid #ddd;text-align:center;line-height:38px;font-size:12px;color:#555}
</style>
</head>
<body>
<div class="abs brand"><span class="brand-mark"></span>velmorino</div>
<div class="abs tagline">The individual greeting cards according to your mood</div>
<div class="abs nav-tab active">PRODUCTS</div>
<div class="abs nav-tab plain">AUTHORS</div>
<div class="abs account">
  <span><svg width="11" height="12" viewBox="0 0 11 12"><circle cx="5.5" cy="3.5" r="3" fill="#b52a1c"/><path d="M0 12c0-4 2-5 5.5-5s5.5 1 5.5 5z" fill="#b52a1c"/></svg> SIGN IN</span>
  <span class="cart"><svg width="20" height="15" viewBox="0 0 20 15"><path d="M0 1h4l2 9h11l2-7H6" fill="none" stroke="#b52a1c" stroke-width="2"/><circle cx="8" cy="13" r="1.5" fill="#b52a1c"/><circle cx="15" cy="13" r="1.5" fill="#b52a1c"/></svg> <b>CART:</b> 0 ITEMS - $0.00</span>
</div>
<div class="abs rule"></div>
<div class="abs panel"></div>

<div class="abs back">◂ Back</div>
<div class="abs crumbs"><b>Home</b> › <b>Products</b> › Designer</div>
<div class="abs info"><svg width="17" height="17" viewBox="0 0 17 17"><circle cx="8.5" cy="8.5" r="7.5" fill="none" stroke="#777"/><path d="M8.5 7v6M8.5 4v1.5" stroke="#777" stroke-width="1.5"/></svg>Info</div>

<div class="abs stage"></div>
<div class="abs toolbar">
  <div class="tool"><svg width="22" height="18" viewBox="0 0 22 18"><path d="M1 1h12v3M7 1v16M4 17h6M16 9v8M12 13h8" stroke="#333" stroke-width="2.4" fill="none"/></svg>Add Text</div>
  <div class="tool"><svg width="18" height="18" viewBox="0 0 18 18"><rect x="1" y="1" width="16" height="16" fill="none" stroke="#333" stroke-width="2"/><path d="M3 15l4-6 3 4 2-2 3 4z" fill="#333"/></svg>Add Image</div>
  <div class="tool"><svg width="18" height="18" viewBox="0 0 18 18"><circle cx="9" cy="9" r="8" fill="none" stroke="#333" stroke-width="1.5"/><path d="M6 6l6 6M12 6l-6 6" stroke="#333" stroke-width="1.5"/></svg>Clear All</div>
  <div class="tool"><svg width="20" height="18" viewBox="0 0 20 18"><path d="M5 1h10v14H5z" fill="none" stroke="#333" stroke-width="1.4"/><circle cx="8" cy="10" r="4" fill="none" stroke="#333" stroke-width="1.4"/><path d="M5 13l-4 4" stroke="#333" stroke-width="1.6"/></svg>Preview</div>
</div>
<div class="abs card-art" role="img" aria-label="Red ornamental card artwork with a framed bouquet of white winter roses, pine cones and holly berries"></div>
<div class="abs side-label">Front Side</div>

<div class="abs hint">
  <h3><svg width="16" height="16" viewBox="0 0 16 16"><circle cx="8" cy="7" r="4" fill="none" stroke="#333"/><path d="M6 12h4M8 0v2M1 7h2M13 7h2M3 2l1.5 1.5M13 2l-1.5 1.5" stroke="#333"/></svg>Hint</h3>
  <span class="close">x</span>
  <p>Lorem Ipsum is simply dummy text of the printing and typesetting industry. Lorem Ipsum has been the industry's standard dummy text ever since the 1500s</p>
</div>

<div class="abs swatches">
  <i style="background:#0a6fd0"></i><i style="background:#f7f000"></i><i style="background:#a9bfdf"></i><i style="background:#ff6a00"></i>
  <i style="background:#fdc52d"></i><i style="background:#e9508c"></i><i style="background:#d40a0a"></i><i style="background:#ff9b00"></i>
  <i style="background:#5a9a0c"></i><i style="background:#3e4150"></i><i style="background:#9a9a9a"></i><i style="background:#9a6535"></i>
  <i style="background:#000"></i><i style="background:#e9508c"></i><i style="background:#d40a0a"></i><i style="background:#efefef"></i>
</div>

<div class="abs tab sides-tab">Sides</div>
<div class="abs sides-box">
  <div class="side on" style="left:15px;top:11px"><svg width="32" height="52" viewBox="0 0 32 52"><path d="M1 8h30v43H1zM1 8l18-7" fill="#fff" stroke="#999"/></svg>Front</div>
  <div class="side" style="left:99px;top:11px"><svg width="36" height="52" viewBox="0 0 36 52"><path d="M1 8h30v43H1zM31 8l3-7v43l-3 7" fill="#fff" stroke="#999"/></svg>Inner Left</div>
  <div class="side" style="left:181px;top:11px"><svg width="36" height="52" viewBox="0 0 36 52"><path d="M5 8h30v43H5zM5 8L2 1v43l3 7" fill="#fff" stroke="#999"/></svg>Inner Right</div>
  <div class="side" style="left:15px;top:101px"><svg width="32" height="52" viewBox="0 0 32 52"><path d="M1 8h30v43H1zM1 8l18-7" fill="#fff" stroke="#999"/></svg>Front</div>
  <div class="side" style="left:99px;top:101px"><svg width="42" height="40" viewBox="0 0 42 40"><path d="M2 14h8l12-10v32L10 26H2z" fill="#fff" stroke="#999"/><path d="M28 12q5 8 0 16M32 8q8 12 0 24M36 4q10 16 0 32" fill="none" stroke="#999"/></svg>Sound</div>
  <div class="side" style="left:181px;top:101px"><svg width="32" height="40" viewBox="0 0 32 40"><rect x="10" y="2" width="10" height="22" rx="5" transform="rotate(35 15 13)" fill="none" stroke="#999" stroke-width="2"/><rect x="12" y="16" width="10" height="22" rx="5" transform="rotate(35 17 27)" fill="none" stroke="#999" stroke-width="2"/></svg>URL</div>
</div>

<div class="abs tab items-tab"><svg width="14" height="16" viewBox="0 0 14 16"><path d="M1 1h12v3M7 1v14M4 15h6" stroke="#333" stroke-width="2.5" fill="none"/></svg>Items</div>
<div class="abs items-box"></div>
<svg class="abs" style="left:817px;top:474px" width="220" height="34" viewBox="0 0 220 34">
  <rect x="0.5" y="0.5" width="33" height="33" fill="#fff" stroke="#ddd"/><rect x="3" y="3" width="28" height="28" fill="#000"/>
  <g stroke="#555"><path d="M56 10h18M56 14h12M56 18h18M56 22h12M56 26h18"/><path d="M107 10h18M110 14h12M107 18h18M110 22h12M107 26h18"/><path d="M158 10h18M164 14h12M158 18h18M164 22h12M158 26h18"/></g>
</svg>
<div class="abs opacity">Opacity</div>
<div class="abs bar"><i></i></div>
<div class="abs pct">80%</div>
<div class="abs fonts-btn">Fonts</div>
<div class="abs textarea"></div>
<div class="abs btn" style="left:817px">CANCEL</div>
<div class="abs btn" style="left:936px">OK</div>
<div class="abs save"><span class="icon"><svg width="28" height="28" viewBox="0 0 28 28"><path d="M2 2h20l4 4v20H2z" fill="none" stroke="#fff" stroke-width="2.5"/><rect x="7" y="2" width="12" height="8" fill="none" stroke="#fff" stroke-width="2"/><path d="M8 18h12M16 15l4 3-4 3" fill="none" stroke="#fff" stroke-width="2"/></svg></span>Save &amp; Continue<svg style="margin-left:30px" width="10" height="18" viewBox="0 0 10 18"><path d="M1 1l8 8-8 8" fill="none" stroke="#e58b80" stroke-width="1.5"/></svg></div>

<div class="abs instructions">
  <h3><svg width="18" height="16" viewBox="0 0 18 16"><circle cx="5" cy="7" r="3" fill="#b52a1c"/><path d="M0 16c0-4 2-5 5-5s5 1 5 5z" fill="#b52a1c"/><rect x="9" y="1" width="8" height="6" fill="none" stroke="#b52a1c"/></svg>Instructions</h3>
  <p>Lorem Ipsum is simply dummy text of the printing and typesetting industry. Lorem Ipsum has been the industry's standard dummy text ever since the 1500s,<br>when an unknown printer took a galley of type and scrambled it to make a type specimen book. It has survived not only five centuries, but also the leap into electronic typesetting, remaining essentially unchanged. It was popularised in the 1960s with the release of Quillmark sheets containing Lorem Ipsum passages, and more recently with desktop publishing software like Bindle PageForge including versions of Lorem Ipsum.</p>
</div>

<div class="abs footer"></div>
<div class="abs col" style="left:111px"><h4>CARDS</h4><ul><li>All cards</li><li>Birthday cards</li><li>Birth cards</li><li>New baby cards</li><li>Get well cards</li><li>Love/Valentine cards</li><li>Just because cards</li></ul></div>
<div class="abs col" style="left:313px"><h4>SPECIAL</h4><ul><li>All cards</li><li>Birthday cards</li><li>Birth cards</li><li>New baby cards</li><li>Get well cards</li><li>Love/Valentine cards</li><li>Just because cards</li></ul></div>
<div class="abs col" style="left:495px"><h4>MORE INFORMATION</h4><ul><li>How it works</li><li>Pricing</li><li>Terms</li></ul></div>
<div class="abs col" style="left:706px"><h4>ABOUT VELMORINO</h4><ul><li>All cards</li><li>Birthday cards</li><li>Birth cards</li><li>New baby cards</li><li>Get well cards</li></ul></div>
<div class="abs col" style="left:898px"><h4>FOLLOW US</h4></div>
<div class="abs social"><span style="background:#3b5a9a">Lumo</span><span style="background:#5b9bd5">Chirpo</span><span style="background:#1a7bbf">Linkra</span></div>
<div class="abs pay"><span>Vexa</span><span>Marquo</span><span>Mestra</span><span>Amerix</span><span>Paynel</span></div>
<div class="abs copy">© 2014 velmorino</div>
</body>
</html>
```